Envelope Design Project for Real Estate

I am looking for an envelope design for a real estate brokerage. I prefer muted colors and the primary colors should be white, maroon (884445) and gray (aaaaaa).
The design is for a #10 universal envelope (psd and jpg files attached for guidelines). There should be full color on the front and back of the envelope.
You can add a return address on the back side along the top flap. Please use a sample address and phone number in the design - the actual information will be provided to the winning designer.

```html
<!DOCTYPE html>
<html lang="en">
<head>
<meta charset="utf-8">
<title>Birch Hollow Realty – #10 Envelope</title>
<link rel="stylesheet" href="https://fonts.googleapis.com/css2?family=Cinzel:wght@400;600&display=swap">
<style>
  :root {
    --backdrop: #a87f25;
    --maroon: #884445;
    --gray: #aaaaaa;
    --gray-flap: #9a9a9a;
    --white: #ffffff;
    --guide-green: #7fd67f;
    --faint: #eeeced;
    --ink: #222222;
  }
  html, body {
    margin: 0;
    width: 1200px;
    height: 686px;
    overflow: hidden;
    background: var(--backdrop);
  }
  .dieline { display: block; width: 1200px; height: 686px; }
  .serif { font-family: "Cinzel", serif; }
  .flap-maroon { fill: var(--maroon); }
  .panel-white { fill: var(--white); }
  .tab-gray { fill: var(--gray-flap); }
  .band-gray { fill: var(--gray); }
  .cut-line { fill: none; stroke: var(--white); stroke-width: 1.6; stroke-dasharray: 5 4; }
  .fold-line { fill: none; stroke: #bbbbbb; stroke-width: 0.8; stroke-dasharray: 2 2; }
  .safe-guide { fill: none; stroke: var(--guide-green); stroke-width: 1; }
  .return-address { fill: var(--white); font-size: 9.5px; letter-spacing: 0.3px; }
  .brand-name { fill: var(--maroon); font-size: 24px; font-weight: 400; }
  .brand-sub { fill: var(--maroon); font-size: 11px; letter-spacing: 3px; }
  .brand-mark { fill: var(--maroon); }
  .contact { fill: var(--ink); font-size: 8px; }
  .contact-label { fill: var(--maroon); font-style: italic; }
  .web { fill: var(--white); font-size: 9px; letter-spacing: 0.4px; }
  .watermark-circle { fill: var(--faint); }
  .back-name { fill: var(--white); font-size: 27px; }
  .back-sub { fill: var(--white); font-size: 12px; letter-spacing: 3px; }
  .back-mark { fill: var(--white); }
</style>
</head>
<body>
<svg class="dieline" viewBox="0 0 1190 680" preserveAspectRatio="none" xmlns="http://www.w3.org/2000/svg">
  <!-- cut outline -->
  <path class="cut-line" d="M276,147 L298,60 Q302,52 312,52 L842,52 Q852,52 856,60 L876,140 L905,140 Q932,140 932,168 L932,380 Q932,398 908,405 L877,412 L872,610 Q870,640 848,640 L304,640 Q282,640 280,610 L275,412 L244,405 Q222,398 222,380 L222,168 Q222,140 250,140 Z"/>

  <!-- top flap with return address -->
  <path class="flap-maroon" d="M282,147 L301,70 Q304,62 314,62 L838,62 Q848,62 851,70 L870,147 Z"/>
  <path class="safe-guide" d="M298,133 L314,73 L838,73 L855,133"/>
  <text class="serif return-address" x="577" y="110" text-anchor="middle">Complex name, Street name City, State, zip code</text>

  <!-- side flaps -->
  <path class="panel-white" d="M282,147 L250,147 Q228,147 228,170 L228,380 Q228,395 248,400 L282,404 Z"/>
  <path class="tab-gray" d="M220,200 Q220,194 228,194 L252,194 Q259,194 259,202 L268,396 Q250,398 236,392 Q220,386 220,376 Z"/>
  <path class="panel-white" d="M870,147 L902,147 Q924,147 924,170 L924,380 Q924,395 904,400 L870,404 Z"/>
  <path class="tab-gray" d="M932,200 Q932,194 924,194 L900,194 Q893,194 893,202 L884,396 Q902,398 916,392 Q932,386 932,376 Z"/>

  <!-- front panel -->
  <rect class="panel-white" x="282" y="147" width="588" height="222"/>
  <line class="fold-line" x1="282" y1="147" x2="870" y2="147"/>
  <line class="fold-line" x1="282" y1="147" x2="282" y2="401"/>
  <line class="fold-line" x1="870" y1="147" x2="870" y2="401"/>

  <!-- faint decorative circle -->
  <circle class="watermark-circle" cx="770" cy="288" r="76"/>

  <!-- brand block -->
  <circle class="brand-mark" cx="381" cy="199" r="40"/>
  <text class="serif brand-name" x="381" y="248" text-anchor="middle">Birch Hollow</text>
  <text class="serif brand-sub" x="381" y="262" text-anchor="middle">REALTY</text>

  <!-- contact -->
  <text class="serif contact" x="331" y="297">Complex name, Street name</text>
  <text class="serif contact" x="331" y="306">City, State, zip code</text>
  <text class="serif contact" x="331" y="323"><tspan class="contact-label">Mobile :</tspan> (410) 555-0142</text>

  <!-- bottom band -->
  <rect class="flap-maroon" x="282" y="369" width="588" height="32"/>
  <polygon class="band-gray" points="718,369 870,369 870,401 750,401"/>
  <line x1="716" y1="369" x2="747" y2="401" stroke="#ffffff" stroke-width="4"/>
  <text class="serif web" x="331" y="387">www.ChesapeakeHomeGuide.com</text>

  <rect class="safe-guide" x="293" y="158" width="566" height="230"/>

  <!-- bottom flap -->
  <path class="flap-maroon" d="M282,401 L870,401 L862,612 Q860,632 840,632 L312,632 Q292,632 290,612 Z"/>
  <path class="safe-guide" d="M297,414 L856,414 L848,556 L302,556 Z"/>
  <g transform="rotate(180 563 475)">
    <circle class="back-mark" cx="563" cy="448" r="44"/>
    <text class="serif back-name" x="563" y="506" text-anchor="middle">Birch Hollow</text>
    <text class="serif back-sub" x="563" y="521" text-anchor="middle">REALTY</text>
  </g>

  <!-- bottom tab -->
  <path class="tab-gray" d="M303,633 L318,584 Q320,578 328,578 L830,578 Q837,578 839,584 L850,633 Z"/>
</svg>
</body>
</html>
```